Brenvick Holdings LLC, new Business cards

I'm moving offices and need new cards. Plus I'm open to modifying the current design of my card. I will keep the logo but would like to explore other layouts and fonts for the design. I've included the current double sided card for reference. I Like the navy color and white. Might be open to grays or silver. Needs to be clean and elegant.

Target Market(s)

Investors, buyers & sellers of private equities and real estate.

Contact Information for Business Card

Brenvick Holdings
Dorian P.K. Halvers, Managing Principal
418 Ostrander Ave., Suite 612
Denver, CO 80319
M: 970-555-0147, O: 303-555-0192
Dorian@brenvickholdings.example
Brenvickholdings.example

Colors
0354a2
ffffff
c4c4c4

Requirements
Must have
• Business card details.
• Logo raised or embossed, it was designed after a wax seal. Current has raised ink.
Nice to have
• Space on card to write additional notes.

```html
<!DOCTYPE html>
<html lang="en">
<head>
<meta charset="utf-8">
<title>Brenvick Holdings – Business Card</title>
<link rel="stylesheet" href="https://fonts.googleapis.com/css2?family=Work+Sans:wght@400;500&display=swap">
<style>
  :root {
    --page-bg: #d9d4cd;
    --card-clear: #ebe8e3;
    --card-edge: #c4c4c4;
    --navy: #2c2b68;
    --navy-deep: #23225a;
    --ink-light: #e4e1ec;
    --ink-soft: #c9c6da;
    --silver: #b9b4ab;
  }
  * { box-sizing: border-box; margin: 0; padding: 0; }
  html, body {
    width: 1200px;
    height: 1047px;
    overflow: hidden;
    background: var(--page-bg);
  }
  .canvas {
    position: relative;
    width: 1200px;
    height: 1047px;
  }
  .business-card {
    position: absolute;
    left: 100px;
    top: 238px;
    width: 1000px;
    height: 570px;
    border-radius: 18px;
    overflow: hidden;
    background: var(--card-clear);
    box-shadow: 0 0 0 1px var(--card-edge);
    font-family: "Work Sans", sans-serif;
  }
  .card-shapes {
    position: absolute;
    inset: 0;
  }
  .card-details {
    position: absolute;
    left: 51px;
    top: 0;
    color: var(--ink-light);
  }
  .holder-name {
    position: absolute;
    top: 80px;
    white-space: nowrap;
    font-size: 27px;
    font-weight: 500;
    letter-spacing: 0.5px;
    text-transform: uppercase;
  }
  .holder-title {
    position: absolute;
    top: 117px;
    white-space: nowrap;
    font-size: 21px;
    color: var(--ink-soft);
    letter-spacing: 0.3px;
  }
  .office-address {
    position: absolute;
    top: 236px;
    font-style: normal;
    font-size: 21px;
    line-height: 33px;
    white-space: nowrap;
    color: var(--ink-soft);
    letter-spacing: 0.3px;
  }
  .contact-list {
    position: absolute;
    top: 372px;
    list-style: none;
    font-size: 21px;
    line-height: 33px;
    white-space: nowrap;
    color: var(--ink-soft);
    letter-spacing: 0.3px;
  }
  .contact-list li {
    display: flex;
    align-items: center;
    gap: 10px;
  }
  .contact-icon {
    width: 14px;
    height: 14px;
    flex: none;
  }
  .brand-mark {
    position: absolute;
    left: 556px;
    top: 245px;
    width: 400px;
    text-align: center;
    font-size: 34px;
    font-weight: 500;
    letter-spacing: 1px;
    color: var(--navy);
  }
</style>
</head>
<body>
<main class="canvas">
  <section class="business-card" aria-label="Brenvick Holdings business card">
    <svg class="card-shapes" width="1000" height="570" viewBox="0 0 1000 570" aria-hidden="true">
      <defs>
        <linearGradient id="navy-panel" x1="0" y1="0" x2="1" y2="1">
          <stop offset="0" stop-color="#2f2e6e"/>
          <stop offset="1" stop-color="#23225a"/>
        </linearGradient>
      </defs>
      <path d="M0 0 H756 A285 285 0 0 0 756 570 H0 Z" fill="url(#navy-panel)"/>
      <circle cx="762" cy="285" r="285" fill="none" stroke="var(--silver)" stroke-width="6"/>
    </svg>

    <div class="card-details">
      <h1 class="holder-name">Dorian P.K. Halvers</h1>
      <p class="holder-title">Managing Principal</p>
      <address class="office-address">
        418 Ostrander Ave., Suite 612<br>
        Denver, CO 80319
      </address>
      <ul class="contact-list">
        <li>
          <svg class="contact-icon" viewBox="0 0 14 14" aria-hidden="true"><path d="M3 1 L5.5 1 L6.5 4 L5 5.2 Q6.3 8 8.8 9 L10 7.5 L13 8.5 L13 11 Q13 13 11 13 Q1 12 1 3 Q1 1 3 1 Z" fill="currentColor"/></svg>
          970-555-0147, O: TBD
        </li>
        <li>
          <svg class="contact-icon" viewBox="0 0 14 14" aria-hidden="true"><rect x="1" y="3" width="12" height="8.5" rx="1" fill="none" stroke="currentColor" stroke-width="1.4"/><path d="M1.5 3.5 L7 8 L12.5 3.5" fill="none" stroke="currentColor" stroke-width="1.4"/></svg>
          Dorian@brenvickholdings.example
        </li>
        <li>
          <svg class="contact-icon" viewBox="0 0 14 14" aria-hidden="true"><circle cx="7" cy="7" r="5.8" fill="none" stroke="currentColor" stroke-width="1.3"/><ellipse cx="7" cy="7" rx="2.5" ry="5.8" fill="none" stroke="currentColor" stroke-width="1.1"/><path d="M1.2 7 H12.8" stroke="currentColor" stroke-width="1.1"/></svg>
          www.Brenvickholdings.example
        </li>
      </ul>
    </div>

    <p class="brand-mark">Brenvick Holdings</p>
  </section>
</main>
</body>
</html>
```